Quarry IT Services Business Card

Quarry IT Services are a Perth based IT Services company. We would like to incorporate our company logo (attached) and stick with the blue that is in that design. I would like a clean look design that isn't too busy, yet creates a lasting image that is instantly recognisable in the recipients mind.

Target Market(s)

The target audience is small/medium business owners.

Industry/Entity Type

Business

Font styles to use
Serif
Sans Serif

Colors

Designer to choose colors to be used in the design.

Requirements
Must have
• The design should include:
Business name: Quarry IT Services
Directors Name: Darren Mowley
Phone Number: 0462 830 514
Email: support@quarryit.com.au
Website: www.quarryit.com.au

```html
<!DOCTYPE html>
<html lang="en">
<head>
<meta charset="utf-8">
<title>Quarry IT Services – Business Card</title>
<link rel="stylesheet" href="https://fonts.googleapis.com/css2?family=Roboto:wght@400;700&display=swap">
<style>
  :root {
    --brand-blue: #1f8fd6;
    --accent-cyan: #36b8ee;
    --card-light: #f4f4f5;
    --card-shade: #dcdde0;
    --panel-dark: #2e2e30;
    --text-dark: #2a2a2c;
    --text-light: #f1f1f1;
    --backdrop: #e4e5e8;
  }
  * { box-sizing: border-box; margin: 0; padding: 0; }
  html, body {
    width: 1200px; height: 768px; overflow: hidden;
    background: var(--backdrop);
    font-family: "Roboto", Arial, sans-serif;
  }
  .sheet {
    width: 1200px; height: 768px;
    display: flex; align-items: center; justify-content: center; gap: 40px;
  }
  .card {
    position: relative;
    width: 540px; height: 328px;
    background: radial-gradient(ellipse at 45% 35%, #ffffff 0%, var(--card-light) 45%, var(--card-shade) 100%);
    box-shadow: 0 6px 18px rgba(0,0,0,.18);
    overflow: hidden;
  }

  /* Front */
  .card-front { display: flex; align-items: center; justify-content: center; }
  .brand { display: flex; align-items: center; gap: 16px; }
  .brand-dot {
    width: 56px; height: 56px; border-radius: 50%;
    background: var(--brand-blue);
  }
  .brand-name {
    color: var(--brand-blue);
    font-weight: 700;
    font-size: 40px;
    letter-spacing: 1px;
    text-transform: uppercase;
  }

  /* Back */
  .card-back .brand { position: absolute; left: 34px; top: 52px; gap: 10px; }
  .card-back .brand-dot { width: 28px; height: 28px; }
  .card-back .brand-name { font-size: 20px; letter-spacing: .5px; }

  .person { position: absolute; right: 40px; top: 30px; text-align: right; }
  .person-name { font-size: 15px; color: var(--text-dark); }
  .person-role { font-size: 12px; color: var(--accent-cyan); margin-top: 2px; }

  .contact-panel {
    position: absolute; bottom: 0;
    width: 178px;
    background: var(--panel-dark);
    color: var(--text-light);
    font-size: 12px;
    display: flex; align-items: flex-end; justify-content: center;
    padding-bottom: 34px;
  }
  .contact-phone { left: 0; top: 236px; }
  .contact-web { left: 181px; top: 206px; }
  .contact-mail { left: 362px; top: 176px; align-items: flex-start; padding-top: 26px; font-size: 11px; }
  .contact-mail .contact-text { margin-top: 0; }
  .contact-web::after, .contact-mail::after {
    content: ""; position: absolute; left: 0; right: 0; bottom: 10px;
    height: 3px; background: var(--accent-cyan);
  }
  .contact-icon {
    position: absolute; top: -18px; left: 50%; transform: translateX(-50%);
    width: 36px; height: 36px;
    background: var(--accent-cyan);
    border: 3px solid #ffffff;
    display: flex; align-items: center; justify-content: center;
  }
  .contact-icon svg { width: 18px; height: 18px; }
</style>
</head>
<body>
<main class="sheet">
  <section class="card card-front" aria-label="Card front">
    <div class="brand">
      <span class="brand-dot"></span>
      <span class="brand-name">Quarry IT Services</span>
    </div>
  </section>

  <section class="card card-back" aria-label="Card back">
    <div class="brand">
      <span class="brand-dot"></span>
      <span class="brand-name">Quarry IT Services</span>
    </div>
    <div class="person">
      <p class="person-name">Darren Mowley</p>
      <p class="person-role">Director</p>
    </div>

    <div class="contact-panel contact-phone">
      <span class="contact-icon">
        <svg viewBox="0 0 24 24" fill="#fff"><path d="M6.6 10.8a15.1 15.1 0 0 0 6.6 6.6l2.2-2.2c.3-.3.7-.4 1-.2 1.1.4 2.3.6 3.6.6.6 0 1 .4 1 1V20c0 .6-.4 1-1 1A17 17 0 0 1 3 4c0-.6.4-1 1-1h3.5c.6 0 1 .4 1 1 0 1.3.2 2.5.6 3.6.1.3 0 .7-.2 1z"/></svg>
      </span>
      <span class="contact-text">0462 830 514</span>
    </div>

    <div class="contact-panel contact-web">
      <span class="contact-icon">
        <svg viewBox="0 0 24 24" fill="none" stroke="#fff" stroke-width="1.8"><circle cx="12" cy="12" r="9"/><ellipse cx="12" cy="12" rx="4" ry="9"/><path d="M3 12h18M4.5 7.5h15M4.5 16.5h15"/></svg>
      </span>
      <span class="contact-text">www.quarryit.com.au</span>
    </div>

    <div class="contact-panel contact-mail">
      <span class="contact-icon">
        <svg viewBox="0 0 24 24" fill="#fff"><path d="M3 6h18v12H3z"/><path d="M3 6l9 7 9-7" fill="none" stroke="#36b8ee" stroke-width="1.6"/></svg>
      </span>
      <span class="contact-text">support@quarryit.com.au</span>
    </div>
  </section>
</main>
</body>
</html>
```